E-Mail-Signatur für einen Fachpflegedienst
Zielgruppe
E-Mail Signatur für einen Fachpflegedienst für außenklinische 1:1 Intensiv- und Beatmungspflege
Aufgabenstellung
E-Mail Signatur zur Nutzung in Microsoft Outlook inkl. Logo.
Vorname, Nachname, E-Mail, Telefon (diese Angaben sollen unsererseits individuell angepasst werden können)
Standort Sindelfingen (inkl. aller Angaben) + Standort Stuttgart (inkl. aller Angaben)
Geschäftsführer, Registernummer, Registergericht
Disclaimer
Beispiel:
Mit freundlichen Grüßen
Torben Wessling LL.M.
Geschäftsführer / Wirtschaftsjurist
E-Mail: tw@kalvoro18.de
Mobil: (0152) 38 91 40 57
kalvoro18 GmbH Sindelfingen
Hagebuttenweg 12
71098 Sindelfingen
Telefon (07031) 48 29 310
Telefax (07031) 48 29 312
kalvoro18 GmbH Stuttgart
Ahornstr. 14
70219 Stuttgart
Telefon: (0711) 83617394
Telefax: (0711) 711 8361736
www.kalvoro18.de
Geschäftsführer: Torben Wessling LL.M.
Registernummer: HRB 482 915
Registergericht: Amtsgericht Brunnfeld
Diese Nachricht enthält vertrauliche Informationen und ist nur für die genannte Person bestimmt. Wenn Sie nicht der genannte Adressat sind, dürfen Sie diese E-Mail nicht verbreiten, verteilen oder kopieren. Sie dürfen keine Anhänge aus der E-Mail verwenden oder weiterleiten. Bitte benachrichtigen Sie den Absender umgehend per E-Mail, wenn Sie diese E-Mail versehentlich erhalten haben, und löschen Sie sie aus Ihrem System.

```html
<!DOCTYPE html>
<html lang="de">
<head>
<meta charset="utf-8">
<title>E-Mail mit Signatur – kalvoro18 GmbH</title>
<link href="https://fonts.googleapis.com/css2?family=Arimo:wght@400;700&display=swap" rel="stylesheet">
<style>
  :root {
    --ink: #111111;
    --muted-line: #e3e3e3;
    --button-border: #cfcfcf;
    --brand-blue: #3d4d8f;
    --brand-red: #c8102e;
    --page: #ffffff;
    --top-bar: #f3f3f3;
  }
  * { margin: 0; padding: 0; box-sizing: border-box; }
  html, body {
    width: 1148px; height: 1200px; overflow: hidden;
    background: var(--page);
    font-family: "Arimo", Arial, sans-serif;
    color: var(--ink);
  }
  .mail { position: relative; width: 1148px; height: 1200px; }
  .top-bar { position: absolute; left: 0; top: 0; width: 100%; height: 8px; background: var(--top-bar); }

  .header-row { position: absolute; left: 0; width: 100%; height: 46px; border-bottom: 1px solid var(--muted-line); }
  .header-row .field-button {
    position: absolute; left: 10px; top: 6px; width: 66px; height: 34px;
    border: 1px solid var(--button-border); border-radius: 3px;
    font-size: 14px; font-weight: 700; display: flex; align-items: center; justify-content: center;
  }
  .header-row .field-value { position: absolute; left: 92px; top: 13px; font-size: 16px; }
  .row-from { top: 13px; } .row-to { top: 59px; } .row-cc { top: 104px; }
  .subject { position: absolute; left: 0; top: 150px; width: 100%; height: 57px; border-bottom: 1px solid var(--muted-line); }
  .subject span { position: absolute; left: 21px; top: 22px; font-size: 16px; }

  .body-text { position: absolute; left: 23px; font-size: 15.5px; line-height: 21px; }

  .brand { position: absolute; left: 22px; top: 705px; height: 66px; display: flex; align-items: center; }
  .brand-mark { width: 40px; height: 40px; background: var(--brand-red); margin-right: 12px; }
  .brand-divider { width: 1px; height: 66px; background: var(--brand-blue); margin-right: 12px; }
  .brand-name { font-size: 22px; color: var(--brand-blue); letter-spacing: 0.5px; }

  .signature {
    position: absolute; left: 76px; top: 796px;
    border-left: 1px solid var(--brand-blue); padding-left: 11px;
    color: var(--brand-blue); font-size: 15.5px; line-height: 21px;
    display: grid; grid-template-columns: 294px auto; row-gap: 21px;
    white-space: nowrap;
  }

  .disclaimer { position: absolute; left: 22px; top: 1064px; width: 560px; font-size: 11.6px; line-height: 15.8px; color: #000; }
</style>
</head>
<body>
<main class="mail">
  <div class="top-bar"></div>

  <div class="header-row row-from"><div class="field-button">Von</div><div class="field-value">Torben.Wessling@kalvoro18.de</div></div>
  <div class="header-row row-to"><div class="field-button">An</div><div class="field-value">kunde@musterpost.de</div></div>
  <div class="header-row row-cc"><div class="field-button">Cc</div></div>
  <div class="subject"><span>Unser Angebot an Sie</span></div>

  <p class="body-text" style="top:241px">Sehr geeehrter Kunde,</p>
  <p class="body-text" style="top:283px">gerne erhalten Sie von uns anbei ein für Sie individuell angepasstes Angebot.</p>
  <p class="body-text" style="top:325px">Si meliora dies, ut vina, poemata reddit, scire velim, chartis pretium quotus arroget annus.<br>scriptor abhinc annos centum qui decidit, inter perfectos veteresque referri debet an<br>inter vilis atque novos? Excludat iurgia finis, “Est vetus atque probus, centum qui perficit annos.</p>
  <p class="body-text" style="top:410px">Quid, qui deperiit minor uno mense vel anno, inter quos referendus erit?<br>Veteresne poetas, an quos et praesens et postera respuat aetas?</p>
  <p class="body-text" style="top:495px">Wir freuen uns auf Ihre Rückmeldung.</p>
  <p class="body-text" style="top:580px">Mit freundlichen Grüßen</p>
  <p class="body-text" style="top:623px">Torben Wessling LL.M.<br>Geschäftsführer / Wirtschaftsjurist</p>

  <div class="brand">
    <div class="brand-mark"></div>
    <div class="brand-divider"></div>
    <div class="brand-name">KALVORO18 GMBH</div>
  </div>

  <section class="signature">
    <div class="location">kalvoro18 GmbH Sindelfingen<br>Hagebuttenweg 12<br>71098 Sindelfingen</div>
    <div class="contact">Telefon (07031) 48 29 310<br>Telefax (07031) 48 29 312<br>Mobil: (0152) 38 91 40 57</div>
    <div class="location">kalvoro18 GmbH Stuttgart<br>Ahornstr. 14<br>70219 Stuttgart</div>
    <div class="contact">Telefon: (0711) 83617394<br>Telefax: (0711) 711 8361736</div>
    <div class="register">Geschäftsführer: Torben Wessling LL.M.<br>Registernummer: HRB 482 915<br>Registergericht: Amtsgericht Brunnfeld</div>
    <div class="contact">E-Mail: tw@kalvoro18.de<br>www.kalvoro18.de</div>
  </section>

  <p class="disclaimer">Diese Nachricht enthält vertrauliche Informationen und ist nur für die genannte Person bestimmt.<br>Wenn Sie nicht der genannte Adressat sind, dürfen Sie diese E-Mail nicht verbreiten, verteilen<br>oder kopieren. Sie dürfen keine Anhänge aus der E-Mail verwenden oder weiterleiten. Bitte<br>benachrichtigen Sie den Absender umgehend per E-Mail, wenn Sie diese E-Mail versehentlich<br>erhalten haben, und löschen Sie sie aus Ihrem System.</p>
</main>
</body>
</html>
```